Our landing page needs to be updated - 1 panel only - SEE NEW MESSAGE AND MOCK UP CONCEPT screenshot

We require the top page of our landing page redesigned to better convey our product offering.

The application is an email marketing platform offering pre-designed and ready-to-use email templates.
The landing page should (a) visually convey our product proposition - ie - display a sample of the email templates (resources provided) and also (b) in copy format explain our product proposition.

There are SIX categories for the templates - on the attached resources these are explained.
You should visit KOVRELL.COM - to see more information (and how bad our current landing page is)

It should be clear there are six categories - their headings are:

1. Message someone
2. Share important information
3. Promote Deals and Special Offers
4. Announce Events
5. Broadcast Newsletters
6. Advertise your Products or Services

These headings are only intended to explain why there are different template designs - they are secondary information

The copy hierarchy is:

Main sell
"Ready-To-Use Email Templates"

Supporting sell

"Insert your images and links then send. It’s that quick and easy.
Beautiful emails deliver better results."

Last sell checklist

"Free image library
300 plus designs
Email analytics"

The images (cropped as required) of our templates are the heroes - the copy should be supporting.

Purple is our primary brand colour

Logo is also provided

At kovrell.com we like "Sign In" being held in a box

Our colour pallet is attached

NB - at Kovrell.com - all panels will remain on the Landing page - other than the top panel - ie - above the fold - this is the one we require redesigning because the image of a female at a keyboard does not convey our product offering.

Button shapes should be consistent with those already on Kovrell.com

Our Font family is LATO

Industry/Entity Type

Marketing

Number of Pages Required

1 page

Requirements
Must have
• Our font family - LATO and our colour pallett
• Our sample email templates
• Top Right - navigation links - "Pricing Create Account Sign In"

```html
<!DOCTYPE html>
<html lang="en">
<head>
<meta charset="utf-8">
<title>Kovrell – Ready-To-Use Email Templates</title>
<link href="https://fonts.googleapis.com/css2?family=Lato:wght@300;400;700;900&display=swap" rel="stylesheet">
<style>
:root{
  --brand:#5b2d91;
  --brand-deep:#3d1b66;
  --brand-light:#8a5cc7;
  --accent:#1ca6e9;
  --ink:#2b2b2b;
  --text:#444;
  --muted:#9a9a9a;
  --line:#e3e3e3;
  --soft:#f3f3f3;
  --white:#fff;
  --footer:#3a3a3a;
  --footer-base:#2c2c2c;
  --step-1:#b5b1ac;
  --step-2:#4b4a5a;
  --step-3:#6b7b9b;
  --step-4:#d6dbe1;
}
*{box-sizing:border-box;margin:0;padding:0}
html,body{width:1200px;height:3789px;overflow:hidden}
body{font-family:'Lato',sans-serif;color:var(--text);background:var(--white);position:relative}
section,header,footer{position:absolute;left:0;width:1200px}
.abs{position:absolute}
ul{list-style:none}

/* hero */
.hero{top:0;height:561px;background:linear-gradient(120deg,var(--brand-deep) 0%,var(--brand) 55%,var(--brand-light) 100%);overflow:hidden}
.brand{font-weight:700;color:var(--white);font-size:50px;letter-spacing:-1px}
.hero .brand{left:45px;top:22px}
.main-nav{right:50px;top:33px;display:flex;gap:36px;align-items:center;font-size:19px;color:var(--white)}
.sign-in{width:100px;height:38px;border:2px solid var(--white);border-radius:8px;display:flex;align-items:center;justify-content:center}
.hero-title{left:45px;top:150px;width:600px;font-size:54px;line-height:1.1;font-weight:900;color:var(--white)}
.hero-copy{left:45px;top:288px;width:560px;font-size:21px;line-height:1.45;color:#ece4f7}
.checklist{left:45px;top:370px;display:flex;gap:28px;font-size:18px;font-weight:700;color:var(--white)}
.checklist li{display:flex;align-items:center;gap:8px}
.btn{background:var(--accent);color:var(--white);border-radius:30px;display:flex;align-items:center;justify-content:center;font-weight:700}
.hero-btn{left:45px;top:436px;width:306px;height:55px;font-size:20px}
.hero-sample{border-radius:6px;box-shadow:0 12px 30px rgba(0,0,0,.35)}
.sample-a{left:690px;top:120px;width:170px;height:400px;background:linear-gradient(180deg,#fff 0 10%,#1e5b93 10% 34%,#dfe9f3 34% 90%,#2a8fd6 90%)}
.sample-b{left:830px;top:95px;width:190px;height:440px;background:linear-gradient(180deg,#9aa0a5 0 26%,#fff 26% 86%,#111 86%);z-index:2}
.sample-c{left:990px;top:140px;width:170px;height:390px;background:linear-gradient(180deg,#f6d3c4 0 30%,#fff 30% 88%,#c9485b 88%)}

/* section headings */
.sec-title{width:1200px;text-align:center;font-size:35px;font-weight:400;color:var(--ink)}

/* categories */
.categories{top:561px;height:748px}
.categories .sec-title{top:42px}
.cat-sub{top:100px;width:1200px;text-align:center;font-size:16px;color:#666}
.cat{width:232px}
.cat-icon{position:absolute;width:76px;height:76px;border-radius:50%;background:var(--white);box-shadow:0 3px 8px rgba(0,0,0,.18);display:flex;align-items:center;justify-content:center}
.cat h3{font-size:17px;font-weight:400;color:var(--ink);margin-bottom:12px}
.cat p{font-size:14.5px;line-height:1.5;color:var(--muted)}
.template-sample{left:475px;top:169px;width:250px;height:528px;background:linear-gradient(180deg,#ffffff 0 9%,#1e5b93 9% 31%,#dfe9f3 31% 92%,#2a8fd6 92%)}

/* steps */
.steps{top:1309px;height:429px;border-top:1px solid var(--line)}
.steps .sec-title{top:52px}
.step-line{top:198px;height:8px;background:#e6e6e6}
.step{width:240px;text-align:center;top:135px}
.step-circle{width:126px;height:126px;border-radius:50%;margin:0 auto 22px;display:flex;align-items:center;justify-content:center}
.step h3{font-size:18px;font-weight:400;color:var(--ink);margin-bottom:6px}
.step p{font-size:14px;line-height:1.4;color:var(--muted)}

/* audience */
.audience{top:1738px;height:712px;background:var(--soft)}
.aud-back{left:114px;top:160px;width:389px;height:205px;background:#d9d9d9}
.aud-sample{left:149px;top:58px;width:318px;height:543px;background:linear-gradient(180deg,#9aa0a5 0 24%,#ffffff 24% 87%,#111 87%)}
.aud-title{left:568px;top:50px;font-size:38px;font-weight:400;color:var(--ink)}
.aud-copy{left:568px;top:114px;width:590px;font-size:13.5px;line-height:1.55;color:var(--muted)}
.accordion{left:568px;top:243px;width:589px;background:var(--white)}
.acc-item{height:57px;border-bottom:1px solid var(--line);display:flex;align-items:center;justify-content:space-between;padding:0 26px;font-size:17px;color:var(--ink);background:#fbfbfb}
.acc-item.open{background:var(--white);border:1px solid var(--line)}
.acc-body{height:117px;padding:24px 26px;font-size:15px;line-height:1.5;color:var(--muted);border:1px solid var(--line);border-top:none}
.acc-toggle{width:26px;height:26px}

/* features */
.features{top:2450px;height:311px}
.features .sec-title{top:50px}
.feature{width:270px}
.feat-num{position:absolute;width:76px;height:76px;border-radius:50%;background:var(--accent);color:var(--white);font-size:30px;display:flex;align-items:center;justify-content:center}
.feature h3{font-size:17px;font-weight:400;color:var(--ink);margin-bottom:10px;line-height:1.3}
.feature p{font-size:14px;line-height:1.45;color:var(--muted)}

/* pricing */
.pricing{top:2761px;height:675px;background:var(--soft)}
.pricing .sec-title{top:50px}
.plan{top:144px;height:472px;background:var(--white);border-radius:16px;box-shadow:0 2px 6px rgba(0,0,0,.08);width:220px}
.plan h3{text-align:center;font-size:18px;font-weight:400;color:var(--ink);margin-top:32px}
.plan .price{text-align:center;font-size:42px;font-weight:700;color:var(--ink);margin-top:14px;padding-bottom:18px;border-bottom:1px solid var(--line)}
.plan ul{padding:22px 18px 0 22px}
.plan li{display:flex;gap:14px;font-size:13.5px;line-height:1.3;color:var(--text);height:57px}
.plan li svg{flex:none;margin-top:2px}
.plan .btn{position:absolute;left:43px;bottom:50px;width:134px;height:36px;font-size:16px}

/* footer */
.site-footer{top:3436px;height:353px;background:var(--footer);color:#ddd}
.site-footer .brand{left:68px;top:40px}
.tagline{left:68px;top:126px;font-size:19px;line-height:1.35;color:#ddd;width:300px}
.socials{left:68px;top:199px;display:flex;gap:30px}
.socials span{width:36px;height:36px;border-radius:50%;background:var(--accent)}
.foot-h{font-size:19px;color:var(--white)}
.quick-h{left:437px;top:32px}
.links{font-size:13.5px;color:#ddd}
.links li{height:27px;display:flex;align-items:center;gap:12px}
.links li::before{content:"›";color:#aaa}
.links-1{left:458px;top:79px}
.links-2{left:620px;top:79px}
.news-h{left:874px;top:32px}
.field{left:874px;width:281px;height:35px;background:#2e2e2e;border:1px solid #444;font-size:13px;color:#888;padding:0 12px;display:flex;align-items:center}
.send{left:874px;top:212px;width:149px;height:31px;font-size:15px}
.copyright{left:0;top:303px;width:1200px;height:50px;background:var(--footer-base);display:flex;align-items:center;justify-content:center;font-size:14px;color:#ccc}
</style>
</head>
<body>

<header class="hero">
  <div class="abs brand">Kovrell</div>
  <nav class="abs main-nav">
    <span>Pricing</span><span>Create Account</span><span class="sign-in">Sign In</span>
  </nav>
  <h1 class="abs hero-title">Ready-To-Use Email Templates</h1>
  <p class="abs hero-copy">Insert your images and links then send. It’s that quick and easy.<br>Beautiful emails deliver better results.</p>
  <ul class="abs checklist">
    <li><svg width="18" height="18" viewBox="0 0 14 14"><path d="M2 7l3 3 7-7" stroke="#fff" stroke-width="2.2" fill="none"/></svg>Free image library</li>
    <li><svg width="18" height="18" viewBox="0 0 14 14"><path d="M2 7l3 3 7-7" stroke="#fff" stroke-width="2.2" fill="none"/></svg>300 plus designs</li>
    <li><svg width="18" height="18" viewBox="0 0 14 14"><path d="M2 7l3 3 7-7" stroke="#fff" stroke-width="2.2" fill="none"/></svg>Email analytics</li>
  </ul>
  <div class="abs btn hero-btn">View our template gallery</div>
  <div class="abs hero-sample sample-a" role="img" aria-label="Sample promotional email template with offer banner and product grid"></div>
  <div class="abs hero-sample sample-b" role="img" aria-label="Sample business letter email template with header photo and dark footer"></div>
  <div class="abs hero-sample sample-c" role="img" aria-label="Sample event announcement email template with banner image"></div>
</header>

<section class="categories">
  <h2 class="abs sec-title">Email templates for every business</h2>
  <p class="abs cat-sub">Professionally designed, responsive, mobile-ready templates.</p>

  <div class="abs cat-icon" style="left:50px;top:216px"><svg width="34" height="34" viewBox="0 0 24 24" fill="#1ca6e9"><path d="M12 3c5 0 9 3.4 9 7.5S17 18 12 18c-1 0-2-.1-2.9-.4L4 20l1.6-4C4 14.6 3 12.6 3 10.5 3 6.4 7 3 12 3z"/><circle cx="8" cy="10.5" r="1.2" fill="#fff"/><circle cx="12" cy="10.5" r="1.2" fill="#fff"/><circle cx="16" cy="10.5" r="1.2" fill="#fff"/></svg></div>
  <div class="abs cat" style="left:150px;top:218px"><h3>Message someone</h3><p>Lorem ipsum dolor sit amet, consecte tur adipiscing elit. Integer arcu ante.</p></div>

  <div class="abs cat-icon" style="left:50px;top:374px"><svg width="34" height="34" viewBox="0 0 24 24" fill="#1ca6e9"><circle cx="12" cy="12" r="10"/><g fill="#fff"><circle cx="15.5" cy="7.5" r="1.8"/><circle cx="8" cy="12" r="1.8"/><circle cx="15.5" cy="16.5" r="1.8"/></g><path d="M15.5 7.5L8 12l7.5 4.5" stroke="#fff" stroke-width="1.3" fill="none"/></svg></div>
  <div class="abs cat" style="left:150px;top:376px"><h3>Share important information</h3><p>Lorem ipsum dolor sit amet, consecte tur adipiscing elit. Integer arcu ante.</p></div>

  <div class="abs cat-icon" style="left:50px;top:532px"><svg width="34" height="34" viewBox="0 0 24 24" fill="none" stroke="#1ca6e9" stroke-width="1.8"><path d="M2 4h3l2.5 11h11l2-8H6.5"/><circle cx="9" cy="19" r="1.5"/><circle cx="17" cy="19" r="1.5"/></svg></div>
  <div class="abs cat" style="left:150px;top:534px"><h3>Promote Deals and Special Offers</h3><p>Lorem ipsum dolor sit amet, consecte tur adipiscing elit. Integer arcu ante.</p></div>

  <div class="abs template-sample" role="img" aria-label="Sample promotional email template with an exclusive promotion banner and a grid of product offers"></div>

  <div class="abs cat-icon" style="left:813px;top:216px"><svg width="34" height="34" viewBox="0 0 24 24" fill="#1ca6e9"><path d="M3 10h4l10-5v14L7 14H3z"/><path d="M7 14l2 6h3l-2-6z"/></svg></div>
  <div class="abs cat" style="left:915px;top:218px"><h3>Announce Events</h3><p>Lorem ipsum dolor sit amet, consecte tur adipiscing elit. Integer arcu ante.</p></div>

  <div class="abs cat-icon" style="left:813px;top:374px"><svg width="34" height="34" viewBox="0 0 24 24" fill="none" stroke="#1ca6e9" stroke-width="1.8"><rect x="4" y="3" width="16" height="18" rx="1"/><rect x="7" y="6" width="5" height="5" fill="#1ca6e9"/><path d="M14 7h3M14 10h3M7 14h10M7 17h10"/></svg></div>
  <div class="abs cat" style="left:915px;top:376px"><h3>Broadcast Newsletters</h3><p>Lorem ipsum dolor sit amet, consecte tur adipiscing elit. Integer arcu ante.</p></div>

  <div class="abs cat-icon" style="left:813px;top:532px"><svg width="34" height="34" viewBox="0 0 24 24" fill="none" stroke="#1ca6e9" stroke-width="2"><path d="M4 20V14M9 20V11M14 20V13M19 20V8"/><path d="M4 10l5-4 5 3 6-5"/></svg></div>
  <div class="abs cat" style="left:915px;top:534px"><h3>Advertise your Products or Services</h3><p>Lorem ipsum dolor sit amet, consecte tur adipiscing elit. Integer arcu ante.</p></div>
</section>

<section class="steps">
  <h2 class="abs sec-title">Beautiful emails by you... in seconds.</h2>
  <div class="abs step-line" style="left:240px;width:160px"></div>
  <div class="abs step-line" style="left:523px;width:154px"></div>
  <div class="abs step-line" style="left:803px;width:144px"></div>

  <div class="abs step" style="left:57px">
    <div class="step-circle" style="background:var(--step-1)"><svg width="50" height="50" viewBox="0 0 24 24" fill="#e9e7e4"><rect x="3" y="3" width="18" height="18"/><rect x="5" y="5" width="14" height="3" fill="#b5b1ac"/><rect x="5" y="10" width="5" height="9" fill="#b5b1ac"/><rect x="12" y="10" width="7" height="2" fill="#b5b1ac"/><rect x="12" y="14" width="7" height="2" fill="#b5b1ac"/></svg></div>
    <h3>Select your template</h3><p>World-class designers have created the largest gallery of beautiful email templates in the world.</p>
  </div>
  <div class="abs step" style="left:340px">
    <div class="step-circle" style="background:var(--step-2)"><svg width="50" height="50" viewBox="0 0 24 24" fill="none" stroke="#fff" stroke-width="1.6"><rect x="4" y="4" width="11" height="11"/><rect x="9" y="9" width="11" height="11"/><path d="M11 11l5 5M16 12v4h-4"/></svg></div>
    <h3>Write your copy</h3><p>Simply edit your copy within our template using our custom designed email builder.</p>
  </div>
  <div class="abs step" style="left:620px">
    <div class="step-circle" style="background:var(--step-3)"><svg width="50" height="50" viewBox="0 0 24 24" fill="none" stroke="#fff" stroke-width="1.6"><rect x="3" y="4" width="18" height="16"/><circle cx="9" cy="9" r="2" fill="#fff"/><path d="M3 18l6-6 4 4 3-3 5 5" fill="#fff"/></svg></div>
    <h3>Add your images</h3><p>Upload images, logos or graphics and link to your website to drive reader interaction.</p>
  </div>
  <div class="abs step" style="left:890px">
    <div class="step-circle" style="background:var(--step-4)"><svg width="50" height="50" viewBox="0 0 24 24" fill="#fff"><path d="M21 3L2 11l7 2 2 7z"/><path d="M21 3L9 13" stroke="#d6dbe1" stroke-width="1"/></svg></div>
    <h3>Add recipients and send!</h3><p>That's it. The fastest and easiest way to create and send stunning email, which get results!</p>
  </div>
</section>

<section class="audience">
  <div class="abs aud-back"></div>
  <div class="abs aud-sample" role="img" aria-label="Sample business email template with a header photo, logo area, letter text and dark footer"></div>
  <h2 class="abs aud-title">Who should use Kovrell?</h2>
  <p class="abs aud-copy">When you need to create and send quickly, or if you don't have the budgets for designers and developers, then Kovrell is a perfect solution. We've already done all the design and html work! In seconds you can select a pre-formatted template and send a beautiful email which will impress your contacts, dramatically increase open rates and make your email messages more effective.</p>
  <div class="abs accordion">
    <div class="acc-item open">Sales &amp; Marketing Teams
      <svg class="acc-toggle" viewBox="0 0 26 26"><circle cx="13" cy="13" r="12" fill="none" stroke="#1ca6e9" stroke-width="2"/><path d="M8 13h10" stroke="#1ca6e9" stroke-width="2"/></svg></div>
    <div class="acc-body">Get better results using world-class email templates incorporating analytics</div>
    <div class="acc-item">Professional Services<svg class="acc-toggle" viewBox="0 0 26 26"><circle cx="13" cy="13" r="11" fill="none" stroke="#aaa" stroke-width="1.3"/><path d="M8 13h10M13 8v10" stroke="#aaa" stroke-width="1.3"/></svg></div>
    <div class="acc-item">Small Business Owners<svg class="acc-toggle" viewBox="0 0 26 26"><circle cx="13" cy="13" r="11" fill="none" stroke="#aaa" stroke-width="1.3"/><path d="M8 13h10M13 8v10" stroke="#aaa" stroke-width="1.3"/></svg></div>
    <div class="acc-item">Healthcare &amp; Education<svg class="acc-toggle" viewBox="0 0 26 26"><circle cx="13" cy="13" r="11" fill="none" stroke="#aaa" stroke-width="1.3"/><path d="M8 13h10M13 8v10" stroke="#aaa" stroke-width="1.3"/></svg></div>
    <div class="acc-item">Entertainment &amp; Retail<svg class="acc-toggle" viewBox="0 0 26 26"><circle cx="13" cy="13" r="11" fill="none" stroke="#aaa" stroke-width="1.3"/><path d="M8 13h10M13 8v10" stroke="#aaa" stroke-width="1.3"/></svg></div>
    <div class="acc-item">Associations &amp; NGOs<svg class="acc-toggle" viewBox="0 0 26 26"><circle cx="13" cy="13" r="11" fill="none" stroke="#aaa" stroke-width="1.3"/><path d="M8 13h10M13 8v10" stroke="#aaa" stroke-width="1.3"/></svg></div>
  </div>
</section>

<section class="features">
  <h2 class="abs sec-title">Product Features include</h2>
  <div class="feat-num" style="left:45px;top:127px">01</div>
  <div class="abs feature" style="left:144px;top:124px"><h3>Analytics</h3><p>Keep track of how your emails perform from your dashboard. From open and click through rates, everything you need is here</p></div>
  <div class="feat-num" style="left:417px;top:127px">02</div>
  <div class="abs feature" style="left:515px;top:118px"><h3>Email scheduling and free image library</h3><p>Set up emails to send anytime day or night weeks in advance. Auto-image and logo saving and free image library included.</p></div>
  <div class="feat-num" style="left:816px;top:127px">03</div>
  <div class="abs feature" style="left:917px;top:124px"><h3>Bulk contacts import</h3><p>One click import of your address book and bulk CSV file import of lists. Create unlimited email broadcast groups.</p></div>
</section>

<section class="pricing">
  <h2 class="abs sec-title">Our pricing</h2>
  <div class="abs plan" style="left:45px">
    <h3>Test Drive</h3><div class="price">FREE</div>
    <ul>
      <li><svg width="14" height="14" viewBox="0 0 14 14"><path d="M2 7l3 3 7-7" stroke="#1ca6e9" stroke-width="2" fill="none"/></svg>Three FREE broadcasts</li>
      <li><svg width="14" height="14" viewBox="0 0 14 14"><path d="M2 7l3 3 7-7" stroke="#1ca6e9" stroke-width="2" fill="none"/></svg>No credit card required</li>
      <li><svg width="14" height="14" viewBox="0 0 14 14"><path d="M2 7l3 3 7-7" stroke="#1ca6e9" stroke-width="2" fill="none"/></svg>1000 free email credits</li>
    </ul>
    <div class="btn">Select</div>
  </div>
  <div class="abs plan" style="left:268px">
    <h3>Pay As You Go</h3><div class="price">$7.95</div>
    <ul>
      <li><svg width="14" height="14" viewBox="0 0 14 14"><path d="M2 7l3 3 7-7" stroke="#1ca6e9" stroke-width="2" fill="none"/></svg>Per broadcast</li>
      <li><svg width="14" height="14" viewBox="0 0 14 14"><path d="M2 7l3 3 7-7" stroke="#1ca6e9" stroke-width="2" fill="none"/></svg>Pay only when you broadcast</li>
      <li><svg width="14" height="14" viewBox="0 0 14 14"><path d="M2 7l3 3 7-7" stroke="#1ca6e9" stroke-width="2" fill="none"/></svg>Cost per email address from 1 cent</li>
    </ul>
    <div class="btn">Select</div>
  </div>
  <div class="abs plan" style="left:490px">
    <h3>BronzeMonthly Plan</h3><div class="price">$9.95</div>
    <ul>
      <li><svg width="14" height="14" viewBox="0 0 14 14"><path d="M2 7l3 3 7-7" stroke="#1ca6e9" stroke-width="2" fill="none"/></svg>Three broadcasts per month</li>
      <li><svg width="14" height="14" viewBox="0 0 14 14"><path d="M2 7l3 3 7-7" stroke="#1ca6e9" stroke-width="2" fill="none"/></svg>Pause or cancel anytime No questions asked</li>
      <li><svg width="14" height="14" viewBox="0 0 14 14"><path d="M2 7l3 3 7-7" stroke="#1ca6e9" stroke-width="2" fill="none"/></svg>Cost per email address from 1 cent</li>
    </ul>
    <div class="btn">Select</div>
  </div>
  <div class="abs plan" style="left:713px">
    <h3>Silver Monthly Plan</h3><div class="price">$12.95</div>
    <ul>
      <li><svg width="14" height="14" viewBox="0 0 14 14"><path d="M2 7l3 3 7-7" stroke="#1ca6e9" stroke-width="2" fill="none"/></svg>Ten broadcasts per month</li>
      <li><svg width="14" height="14" viewBox="0 0 14 14"><path d="M2 7l3 3 7-7" stroke="#1ca6e9" stroke-width="2" fill="none"/></svg>Pause or cancel anytime No questions asked</li>
      <li><svg width="14" height="14" viewBox="0 0 14 14"><path d="M2 7l3 3 7-7" stroke="#1ca6e9" stroke-width="2" fill="none"/></svg>Cost per email address from 1 cent</li>
    </ul>
    <div class="btn">Select</div>
  </div>
  <div class="abs plan" style="left:936px">
    <h3>Gold Monthly Plan</h3><div class="price">$24.95</div>
    <ul>
      <li><svg width="14" height="14" viewBox="0 0 14 14"><path d="M2 7l3 3 7-7" stroke="#1ca6e9" stroke-width="2" fill="none"/></svg>100 broadcasts per month</li>
      <li><svg width="14" height="14" viewBox="0 0 14 14"><path d="M2 7l3 3 7-7" stroke="#1ca6e9" stroke-width="2" fill="none"/></svg>Pause or cancel anytime No questions asked</li>
      <li><svg width="14" height="14" viewBox="0 0 14 14"><path d="M2 7l3 3 7-7" stroke="#1ca6e9" stroke-width="2" fill="none"/></svg>Cost per email address from 1 cent</li>
    </ul>
    <div class="btn">Select</div>
  </div>
</section>

<footer class="site-footer">
  <div class="abs brand">Kovrell</div>
  <p class="abs tagline">When you need quick, easy &amp; impressive email</p>
  <div class="abs socials" aria-label="Social links"><span></span><span></span><span></span><span></span></div>
  <h4 class="abs foot-h quick-h">Quick Links</h4>
  <ul class="abs links links-1"><li>Pricing</li><li>Free Trial</li><li>Services</li><li>Events</li><li>Newsletters</li><li>Blog</li></ul>
  <ul class="abs links links-2"><li>Designer's</li><li>Toolkit Support</li><li>Terms &amp; Conditions</li><li>Privacy Policy</li><li>Contact</li></ul>
  <h4 class="abs foot-h news-h">Newsletter</h4>
  <div class="abs field" style="top:91px">Your Name</div>
  <div class="abs field" style="top:146px">Your Email</div>
  <div class="abs btn send">SEND</div>
  <div class="abs copyright">© Copyrighted All rights reserved 2017</div>
</footer>

</body>
</html>
```